Business card for my company-RMK Design Studio

I do not have a logo-I like red and keeping it clean. Information that should be on the card:
Tom Brakefield AIA
Architecture Planning Interiors
Cell Phone-614.492.5068
email-rmkarchitect1@lunvale.com
www.rmkdesignstudio.net

```html
<!DOCTYPE html>
<html lang="en">
<head>
<meta charset="utf-8">
<title>RMK Design Studio – Business Card</title>
<link rel="stylesheet" href="https://fonts.googleapis.com/css2?family=Montserrat:wght@800&family=Rubik:wght@400;500&display=swap">
<style>
  :root {
    --brand-red: #e01f29;
    --brand-red-deep: #c91d27;
    --ink: #2a2a2a;
    --paper: #ffffff;
    --backdrop: #2c2c2c;
  }
  * { box-sizing: border-box; margin: 0; padding: 0; }
  html, body { width: 1200px; height: 1200px; overflow: hidden; }
  body {
    background: var(--backdrop);
    display: flex;
    flex-direction: column;
    align-items: center;
    justify-content: center;
    gap: 80px;
  }
  .card {
    width: 840px;
    height: 480px;
    position: relative;
    box-shadow: 0 18px 40px rgba(0,0,0,0.45);
  }
  .card-front {
    background: radial-gradient(ellipse at 60% 45%, var(--brand-red) 0%, var(--brand-red-deep) 100%);
    display: flex;
    flex-direction: column;
    align-items: center;
    justify-content: center;
    color: var(--paper);
  }
  .studio-name {
    font-family: "Montserrat", sans-serif;
    font-weight: 800;
    font-size: 52px;
    letter-spacing: 1px;
  }
  .studio-url {
    font-family: "Rubik", sans-serif;
    font-weight: 400;
    font-size: 20px;
    letter-spacing: 7px;
    margin-top: 10px;
  }
  .card-back {
    background: var(--paper);
    display: flex;
    align-items: center;
    padding: 0 60px;
  }
  .identity {
    width: 390px;
    text-align: right;
    padding-right: 36px;
    margin-top: -50px;
  }
  .person-name {
    font-family: "Montserrat", sans-serif;
    font-weight: 800;
    font-size: 38px;
    color: var(--ink);
  }
  .person-role {
    font-family: "Rubik", sans-serif;
    font-size: 17px;
    color: var(--brand-red);
    margin-top: 4px;
  }
  .divider {
    width: 2px;
    height: 160px;
    background: var(--ink);
    align-self: center;
    margin-top: 40px;
  }
  .contact-list {
    list-style: none;
    padding-left: 30px;
    margin-top: 110px;
    font-family: "Rubik", sans-serif;
    font-size: 19px;
    color: var(--ink);
  }
  .contact-item {
    display: flex;
    align-items: flex-start;
    gap: 14px;
    margin-bottom: 12px;
    line-height: 1.3;
  }
  .contact-icon { width: 24px; height: 24px; flex: none; fill: var(--brand-red); }
</style>
</head>
<body>
  <section class="card card-front">
    <h1 class="studio-name">RMK DESIGN STUDIO</h1>
    <p class="studio-url">WWW.RMKDESIGNSTUDIO.NET</p>
  </section>

  <section class="card card-back">
    <div class="identity">
      <h2 class="person-name">Tom Brakefield AIA</h2>
      <p class="person-role">Architecture Planning Interiors</p>
    </div>
    <div class="divider"></div>
    <ul class="contact-list">
      <li class="contact-item">
        <svg class="contact-icon" viewBox="0 0 24 24"><path d="M12 2a7 7 0 0 0-7 7c0 5 7 13 7 13s7-8 7-13a7 7 0 0 0-7-7zm0 9.5A2.5 2.5 0 1 1 12 6.5a2.5 2.5 0 0 1 0 5z"/></svg>
        <span>418 Harlow Ave. #112 Ridgeport,<br>Ohio 43210</span>
      </li>
      <li class="contact-item">
        <svg class="contact-icon" viewBox="0 0 24 24"><path d="M7 1h10a2 2 0 0 1 2 2v18a2 2 0 0 1-2 2H7a2 2 0 0 1-2-2V3a2 2 0 0 1 2-2zm0 3v15h10V4H7z"/></svg>
        <span>614.492.5068</span>
      </li>
      <li class="contact-item">
        <svg class="contact-icon" viewBox="0 0 24 24"><path d="M2 5h20v14H2V5zm2 2v.5l8 5.5 8-5.5V7H4z"/></svg>
        <span>rmkarchitect1@lunvale.com</span>
      </li>
      <li class="contact-item">
        <svg class="contact-icon" viewBox="0 0 24 24"><path d="M12 2a10 10 0 1 0 0 20 10 10 0 0 0 0-20zm6.9 6h-3a15 15 0 0 0-1.4-4 8 8 0 0 1 4.4 4zM12 4c.8 1.1 1.5 2.5 1.9 4h-3.8c.4-1.5 1.1-2.9 1.9-4zM4.3 14a8 8 0 0 1 0-4h3.4a16 16 0 0 0 0 4H4.3zm.8 2h3a15 15 0 0 0 1.4 4 8 8 0 0 1-4.4-4zm3-8h-3a8 8 0 0 1 4.4-4 15 15 0 0 0-1.4 4zM12 20c-.8-1.1-1.5-2.5-1.9-4h3.8c-.4 1.5-1.1 2.9-1.9 4zm2.3-6H9.7a14 14 0 0 1 0-4h4.6a14 14 0 0 1 0 4zm.2 6a15 15 0 0 0 1.4-4h3a8 8 0 0 1-4.4 4zm1.8-6a16 16 0 0 0 0-4h3.4a8 8 0 0 1 0 4h-3.4z"/></svg>
        <span>www.rmkdesignstudio.net</span>
      </li>
    </ul>
  </section>
</body>
</html>
```